Web Design Project

We need a web design for a new service offered to people who travel and make reservation for hotels.

The name of the site will be valisebleuepratique.com (valise-bleue-pratique.com in english : Blue handy suitcase)

The service is mostly for users that already have made their reservation for a hotel but have not stayed there yet. We are inviting them to transfer the hotel/travel agency confirmation email to us or to fill in a form about how much they paid and what hotel they want to stay at.

The idea is for us to analyse the price the user is paying for the room, if the reservation can be cancelled and if so, if we can find cheaper. If so, we will send an email back with the best price we have found.

The secondary service is for people who did not make hotel reservation yet by asking what hotel they would like to stay and for how many nights. It is the same as above.

The source of trafic will be google adwords, so I want the page to be minimal and chic. Even though we are in the cheap and discounts universe, I don't want the user to be lost by multiple offers.

In term of design, I like pretty much the site http://lnk.example-short.net/k4Tz
Please find description bellow

Home :

Image of someone saving money

Main texte :

Le même hôtel, la même chambre, les mêmes dates
les mêmes conditions... juste moins cher !
(for your understanding, in english : The same hotel, the same room, the same dates, the same conditions.. Just cheaper !!)

1. Nous trouvons moins cher
2. Vous annulez votre ancienne réservation
3. Vous réservez avec le nouveau tarif

Button ;
Transférer votre email de réservation à contact@valisebleuepratique.com
ou cliquez ici et remplissez le formulaire
(for your understanding, in english : Transfer your reservation email to contact@valisebleuepratique.com or click here to fill form)

Under :

= Réponse sous 24h
Nous travaillons 7j/7 pour vous
(eng : Reply in 24h / We work 7/7 for you)

= Aucune obligation
Nous vous proposons un meilleur tarif mais aucune obligation
(eng : No obligation / we will offer a better price but no obligation for you)

= Service totalement gratuit
Changer votre réservation ne vous coutera rien chez nous
(eng : totally free service, won't cost you anything)

MENU :

ACCUEIL (eng : Home)
COMMENT CA MARCHE(eng : How does it work)
AIDE/FAQ (eng : Help / FAQ)
A PROPOS (eng : WHO WE ARE)
TÉMOIGNAGE (eng : TESIMONIES)
CONTACT

I am requiring 6 pages to be done. One for each menu.

R.

Target Market(s)

Travellers

Industry/Entity Type

Hotel

Requirements
Must have
• White background
Nice to have
• Human caracters drawn like on http://lnk.example-short.net/k4Tz
Should not have
• A messy and overcharged design

```html
<!DOCTYPE html>
<html lang="en">
<head>
<meta charset="utf-8">
<title>Valise bleue pratique – Same hotel, just cheaper</title>
<link href="https://fonts.googleapis.com/css2?family=Open+Sans:ital,wght@0,400;0,600;0,700;1,600;1,700&family=PT+Sans:wght@400;700&display=swap" rel="stylesheet">
<style>
:root{
  --dark:#4a4a4a;
  --darker:#333;
  --red:#d44a2e;
  --red-deep:#c23a1f;
  --panel:#dcdcdc;
  --panel-line:#a9a9a9;
  --field:#efefef;
  --field-line:#d4d4d4;
  --text:#222;
  --muted:#555;
  --white:#fff;
}
*{box-sizing:border-box;margin:0;padding:0}
html,body{width:1093px;height:1200px;overflow:hidden;background:var(--white)}
body{position:relative;font-family:"Open Sans",Arial,sans-serif;color:var(--text)}
.abs{position:absolute}

/* header */
.site-header{left:0;top:0;width:1093px;height:80px;background:var(--dark);border-bottom:2px solid var(--red)}
.brand{left:43px;top:22px;font-size:30px;font-weight:400;color:var(--white);letter-spacing:-.3px}
.contact-line{top:4px;font-size:17px;font-weight:600;color:var(--white);display:flex;align-items:center;gap:9px;white-space:nowrap}
.contact-phone{left:528px}
.contact-email{right:40px}
.contact-icon{width:24px;height:24px;background:#cfd8e4;border-radius:3px;display:flex;align-items:center;justify-content:center}
.main-nav{top:50px;font-size:15px;font-weight:600;color:var(--white)}
.nav-current::after{content:"";position:absolute;left:50%;top:27px;margin-left:-5px;border:5px solid transparent;border-bottom-color:var(--red)}

/* hero */
.hero{left:0;top:80px;width:1093px;height:394px;background:linear-gradient(#fbfbfb,#ececec);border-bottom:3px solid #555}
.hero-art{left:43px;top:140px;width:482px;height:252px;background:linear-gradient(180deg,#e6e6e6 0%,#d9d9d9 55%,#cfcfcf 100%)}
.step{top:15px;height:33px;color:var(--white);font-family:"PT Sans",sans-serif;font-weight:700;font-size:19px;line-height:33px}
.step svg{position:absolute;left:0;top:0}
.step span{position:relative;padding-left:24px}
.check-list{left:557px;top:69px;list-style:none;font-family:"PT Sans",sans-serif;font-weight:700;font-size:20px;color:var(--red)}
.check-list li{height:32px;display:flex;align-items:center;gap:9px}
.tagline{left:821px;top:158px;font-size:26px;font-weight:700;font-style:italic;color:var(--dark)}
.transfer-label{left:560px;top:205px;font-size:19px;color:var(--muted)}
.email-field{left:558px;top:240px;width:324px;height:32px;background:var(--field);border:1px solid #bbb;border-radius:3px}
.reply-note{left:884px;top:254px;font-size:12px;font-weight:600;color:var(--muted)}
.reply-note b{color:var(--red)}
.btn{height:33px;border-radius:3px;color:var(--white);font-size:19px;text-align:center;line-height:32px}
.btn-submit{left:562px;top:287px;width:114px;background:linear-gradient(#d9502f,var(--red-deep));border:1px solid #9c2c14}
.btn-form{left:727px;top:288px;width:105px;background:linear-gradient(#444,#1c1c1c);border:1px solid #111}
.or{left:688px;top:291px;font-size:19px;font-weight:700;color:var(--muted)}
.free-ribbon{left:560px;top:348px;width:402px;height:33px;font-family:"PT Sans",sans-serif;font-size:17px;color:var(--white);line-height:33px}
.free-ribbon svg{position:absolute;left:0;top:0}
.free-ribbon span{position:relative;padding-left:22px}

/* search */
.search-box{left:32px;top:488px;width:418px;height:339px;background:var(--dark)}
.search-title{left:14px;top:8px;font-size:26px;color:var(--white)}
.search-form{left:11px;top:48px;width:394px;height:276px;background:var(--white)}
.label{font-size:14px;color:var(--text)}
.field{height:24px;background:var(--field);border:1px solid var(--field-line);font-size:13px;color:#888;padding:3px 10px}
.select{width:45px;height:24px;background:var(--field);border:1px solid var(--field-line);font-size:14px;padding:2px 10px;display:flex;justify-content:space-between;align-items:center}
.btn-search{left:136px;top:234px;width:119px;height:31px;background:var(--red);color:var(--white);font-weight:700;font-size:18px;text-align:center;line-height:31px}

/* testimonial */
.clients{left:32px;top:832px;width:418px;height:133px;background:var(--red);color:var(--white)}
.clients-art{left:11px;top:30px;width:104px;height:89px;border:1px solid #222;background:linear-gradient(135deg,#f2dccb,#e9b9b0 60%,#cfe0c3)}
.clients-title{left:132px;top:0;font-size:26px}
.clients-quote{left:132px;top:38px;width:275px;font-size:13px;font-weight:600;font-style:italic;line-height:17px;text-align:justify}

/* featured */
.panel{background:var(--panel);border:1px solid var(--panel-line)}
.featured{left:470px;top:488px;width:591px;height:237px}
.panel-title{left:13px;top:2px;font-size:28px;color:var(--red)}
.city{top:47px;width:124px;text-align:center}
.city-photo{width:124px;height:120px}
.city-name{margin-top:3px;font-size:15px;font-weight:700;color:#000}
.city-price{font-size:14px;color:#000}
.city-price b{color:var(--red)}
.destinations{left:470px;top:736px;width:591px;height:228px}
.dest-col{top:57px;list-style:none;font-size:11.5px;color:var(--text)}
.dest-col li{height:25.7px}

/* partners */
.partner{top:1007px;height:53px}

/* footer */
.site-footer{left:0;top:1090px;width:1093px;height:110px;border-top:2px solid #555;background:linear-gradient(#fff,#ececec)}
.footer-nav{top:12px;font-size:14px;color:var(--muted)}
.copyright{right:14px;top:86px;font-size:11.5px;color:var(--darker)}
</style>
</head>
<body>

<header class="site-header abs">
  <div class="brand abs">Valise bleue pratique</div>
  <div class="contact-line contact-phone abs">
    <span class="contact-icon"><svg width="16" height="16" viewBox="0 0 16 16"><path d="M3 2h3l1 3-2 1a8 8 0 0 0 5 5l1-2 3 1v3c-7 1-12-4-11-11z" fill="#2e4b72"/></svg></span>
    201 300 5550 0147
  </div>
  <div class="contact-line contact-email abs">
    <span class="contact-icon"><svg width="18" height="14" viewBox="0 0 18 14"><rect x="1" y="1" width="16" height="12" fill="none" stroke="#2e4b72" stroke-width="1.6"/><path d="M1 1l8 7 8-7" fill="none" stroke="#2e4b72" stroke-width="1.6"/></svg></span>
    contact@valisebleuepratique.com
  </div>
  <nav>
    <span class="main-nav nav-current abs" style="left:482px">Home</span>
    <span class="main-nav abs" style="left:554px">How does it work</span>
    <span class="main-nav abs" style="left:715px">Faq</span>
    <span class="main-nav abs" style="left:765px">Who we are</span>
    <span class="main-nav abs" style="left:877px">Testimonial</span>
    <span class="main-nav abs" style="left:991px">Contact</span>
  </nav>
</header>

<section class="hero abs">
  <div class="hero-art abs" role="img" aria-label="Cheerful cartoon businessman in a suit in front of a pale city skyline"></div>

  <div class="step abs" style="left:43px;width:250px">
    <svg width="250" height="33"><polygon points="0,0 235,0 250,16.5 235,33 0,33" fill="var(--red)"/></svg>
    <span>We find cheaper</span>
  </div>
  <div class="step abs" style="left:288px;width:324px">
    <svg width="324" height="33"><polygon points="0,0 309,0 324,16.5 309,33 0,33 13,16.5" fill="var(--red)"/></svg>
    <span>You cancel your old reservation</span>
  </div>
  <div class="step abs" style="left:607px;width:311px">
    <svg width="311" height="33"><polygon points="0,0 296,0 311,16.5 296,33 0,33 13,16.5" fill="var(--red)"/></svg>
    <span>You book with the new tariff</span>
  </div>

  <ul class="check-list abs">
    <li><svg width="20" height="18" viewBox="0 0 20 18"><rect x="1" y="4" width="13" height="13" fill="none" stroke="var(--red)" stroke-width="2"/><path d="M4 9l4 4 10-12" fill="none" stroke="var(--red)" stroke-width="2.6"/></svg>the same hotel,</li>
    <li><svg width="20" height="18" viewBox="0 0 20 18"><rect x="1" y="4" width="13" height="13" fill="none" stroke="var(--red)" stroke-width="2"/><path d="M4 9l4 4 10-12" fill="none" stroke="var(--red)" stroke-width="2.6"/></svg>the same room,</li>
    <li><svg width="20" height="18" viewBox="0 0 20 18"><rect x="1" y="4" width="13" height="13" fill="none" stroke="var(--red)" stroke-width="2"/><path d="M4 9l4 4 10-12" fill="none" stroke="var(--red)" stroke-width="2.6"/></svg>the same dates,</li>
    <li><svg width="20" height="18" viewBox="0 0 20 18"><rect x="1" y="4" width="13" height="13" fill="none" stroke="var(--red)" stroke-width="2"/><path d="M4 9l4 4 10-12" fill="none" stroke="var(--red)" stroke-width="2.6"/></svg>the same conditions..</li>
  </ul>
  <div class="tagline abs">JUST CHEAPER !!</div>

  <div class="transfer-label abs">Transfer your reservation email</div>
  <div class="email-field abs"></div>
  <div class="reply-note abs">(Reply in <b>24</b>hrs)</div>
  <div class="btn btn-submit abs">Submit</div>
  <div class="or abs">or</div>
  <div class="btn btn-form abs">Fill form</div>

  <div class="free-ribbon abs">
    <svg width="402" height="33"><polygon points="0,0 402,0 388,16.5 402,33 0,33 12,16.5" fill="var(--dark)"/></svg>
    <span>Totally free service, won't cost you anything</span>
  </div>
</section>

<section class="search-box abs">
  <div class="search-title abs">Search for hotel</div>
  <form class="search-form abs">
    <div class="label abs" style="left:16px;top:16px">Where are you going</div>
    <div class="field abs" style="left:17px;top:40px;width:303px">City name</div>
    <div class="label abs" style="left:17px;top:90px">Check-in</div>
    <div class="field abs" style="left:17px;top:112px;width:133px">dd/mm/yy</div>
    <div class="label abs" style="left:172px;top:90px">Check-out</div>
    <div class="field abs" style="left:172px;top:114px;width:133px">dd/mm/yy</div>
    <div class="label abs" style="left:17px;top:163px">Rooms</div>
    <div class="select abs" style="left:17px;top:188px">1<svg width="9" height="16"><path d="M4.5 1L8 6H1zM4.5 15L8 10H1z" fill="#888"/></svg></div>
    <div class="label abs" style="left:172px;top:165px">Adults</div>
    <div class="select abs" style="left:172px;top:188px">2<svg width="9" height="16"><path d="M4.5 1L8 6H1zM4.5 15L8 10H1z" fill="#888"/></svg></div>
    <div class="label abs" style="left:259px;top:165px">Children</div>
    <div class="select abs" style="left:259px;top:188px">0<svg width="9" height="16"><path d="M4.5 1L8 6H1zM4.5 15L8 10H1z" fill="#888"/></svg></div>
    <div class="btn-search abs">Search</div>
  </form>
</section>

<section class="clients abs">
  <div class="clients-art abs" role="img" aria-label="Cartoon of someone dropping a coin into a piggy bank"></div>
  <div class="clients-title abs">Our clients say:</div>
  <p class="clients-quote abs">“Lorem ipsum dolor sit amet, nobis alterum ei cum. Usu te iusto dolorem, ad eum modus vocibus minimum. ”</p>
</section>

<section class="featured panel abs">
  <h2 class="panel-title abs" style="font-weight:400">Featured budget hotels</h2>
  <div class="city abs" style="left:15px"><div class="city-photo" role="img" aria-label="Budapest riverside with parliament building" style="background:linear-gradient(#b9d6ee,#8aa3a8 55%,#3f5e6c)"></div><div class="city-name">Budapest</div><div class="city-price">from <b>$22</b></div></div>
  <div class="city abs" style="left:167px"><div class="city-photo" role="img" aria-label="Hong Kong skyline over the harbour" style="background:linear-gradient(#a8c9e6,#7d8f9c 50%,#3e6d8a)"></div><div class="city-name">Hongkong</div><div class="city-price">from <b>$15</b></div></div>
  <div class="city abs" style="left:310px"><div class="city-photo" role="img" aria-label="Waterfront city skyline under blue sky" style="background:linear-gradient(#5f9fd8,#b9c6cf 55%,#2a6f94)"></div><div class="city-name">Manchester</div><div class="city-price">from <b>$50</b></div></div>
  <div class="city abs" style="left:455px"><div class="city-photo" role="img" aria-label="Venice canal with gondola and bridge" style="background:linear-gradient(#8dc3ea,#d8b98c 55%,#3f7b7a)"></div><div class="city-name">Venice</div><div class="city-price">from <b>$70</b></div></div>
</section>

<section class="destinations panel abs">
  <h2 class="panel-title abs" style="left:18px;top:8px;font-weight:400">Top&nbsp; hotel destination</h2>
  <ul class="dest-col abs" style="left:24px"><li>Sydney Hotels</li><li>Paris Hotels</li><li>Brisbane Hotels</li><li>Bangkok Hotels</li><li>Las Vegas Hotels</li><li>Hawaii Hotels</li></ul>
  <ul class="dest-col abs" style="left:156px"><li>Melbourne Hotels</li><li>Phuket Hotels</li><li>Perth Hotels</li><li>Kuala Lumpur Hotels</li><li>Los Angeles Hotels</li><li>Fiji Hotels</li></ul>
  <ul class="dest-col abs" style="left:313px;top:56px"><li>Bali Hotels</li><li>London Hotels</li><li>Cairns Hotels</li><li>Hong Kong Hotels</li><li>San Francisco Hotels</li><li>Auckland Hotels</li></ul>
  <ul class="dest-col abs" style="left:471px;top:56px"><li>Gold Coast Hotels</li><li>Singapore Hotels</li><li>Port Douglas Hotels</li><li>Dubai Hotels</li><li>New York Hotels</li><li>Tokyo Hotels</li></ul>
</section>

<section aria-label="Partner hotel chains">
  <div class="partner abs" style="left:80px;top:1022px;width:96px;height:26px;background:#222;border-radius:3px"></div>
  <div class="partner abs" style="left:205px;width:51px;background:#1d3f7a"></div>
  <div class="partner abs" style="left:283px;top:1020px;width:102px;height:28px;background:#8c8c8c"></div>
  <div class="partner abs" style="left:411px;top:1008px;width:51px;height:51px;border-radius:50%;background:#3c3c3c"></div>
  <div class="partner abs" style="left:505px;top:1010px;width:70px;height:48px;background:#2a4f9c"></div>
  <div class="partner abs" style="left:615px;width:55px;background:#334a6a"></div>
  <div class="partner abs" style="left:695px;top:1009px;width:100px;height:50px;background:#6e1a3d"></div>
  <div class="partner abs" style="left:799px;top:1009px;width:98px;height:50px;background:#9fc6b6"></div>
  <div class="partner abs" style="left:901px;top:1009px;width:99px;height:50px;background:#8fa9de;border-radius:3px"></div>
</section>

<footer class="site-footer abs">
  <span class="footer-nav abs" style="left:28px">Home</span>
  <span class="footer-nav abs" style="left:86px">How does it work</span>
  <span class="footer-nav abs" style="left:219px">Faq</span>
  <span class="footer-nav abs" style="left:257px">Who we are</span>
  <span class="footer-nav abs" style="left:349px">Testimonial</span>
  <span class="footer-nav abs" style="left:443px">Contact</span>
  <span class="footer-nav abs" style="left:507px">User Agreement</span>
  <span class="footer-nav abs" style="left:627px">Privacy policy</span>
  <span class="copyright abs">Copyright 2012 Valise bleue pratique. All rights reserved.</span>
</footer>

</body>
</html>
```